Sing Along Green Goat

We need a couple of brochures made up for a new company Sing Along Green goat. We are offer a creative consulting business for early childhood.

The first brochures is "about us" the presenters of the workshops. We would prefer a coloured background, something funky and bold, even if we could included the colours of the cow's legs. If someone knows how to remove the white background on the logo, that would also be fantastic.
I also like the idea of photo's of the presenters. I will get them too you ASAP
The second brochure is of up coming workshops!

Could we also include on both Brochures: Website: www.singalonggreengoats.com.au
email: info@singalonggreengoats.com.au
Address: 417 Marrabel Street
Caulfield Vic 3162
Phone: 0462 817 904
A.B.N 62-394-257-118

Target Market(s)

Teacher's, early childhood professionals. Owner/operator of childcare. Parent's, after school care.

Industry/Entity Type

Business

```html
<!DOCTYPE html>
<html lang="en">
<head>
<meta charset="utf-8">
<title>Sing Along Green Goat — Brochure Cover</title>
<link rel="stylesheet" href="https://fonts.googleapis.com/css2?family=Fredoka:wght@500&display=swap">
<style>
  :root {
    --forest-green: #1a8705;
    --cocoa-brown: #512400;
    --tangerine: #ff4a00;
    --lime: #56c500;
    --navy: #11058a;
    --paper: #ffffff;
    --sky-line: #33d9f2;
  }
  html, body {
    margin: 0;
    padding: 0;
    overflow: hidden;
    background: var(--paper);
  }
  .brochure {
    position: relative;
    width: 1200px;
    height: 849px;
    overflow: hidden;
  }
  .brochure-panels {
    position: absolute;
    inset: 0;
    display: block;
  }
  .panel-forest { fill: var(--forest-green); }
  .wedge-brown { fill: var(--cocoa-brown); }
  .panel-lime { fill: var(--lime); }
  .wedge-orange { fill: var(--tangerine); }
  .panel-paper { fill: var(--paper); }
  .wedge-navy { fill: var(--navy); }

  .brand-card {
    position: absolute;
    left: 818px;
    top: 31px;
    width: 347px;
    height: 535px;
  }
  .brand-frame {
    position: absolute;
    inset: 0;
  }
  .brand-lockup {
    position: absolute;
    left: 24px;
    right: 24px;
    top: 196px;
    display: flex;
    align-items: center;
    justify-content: center;
    gap: 12px;
  }
  .brand-mark {
    flex: none;
    width: 22px;
    height: 22px;
    border-radius: 50%;
    background: var(--navy);
  }
  .brand-name {
    margin: 0;
    font-family: "Fredoka", sans-serif;
    font-weight: 500;
    font-size: 22px;
    line-height: 1;
    letter-spacing: 1px;
    color: var(--navy);
    text-transform: uppercase;
    white-space: nowrap;
  }
  .brand-tagline {
    position: absolute;
    left: 24px;
    right: 24px;
    top: 236px;
    margin: 0;
    text-align: center;
    font-family: "Fredoka", sans-serif;
    font-weight: 500;
    font-size: 12px;
    line-height: 1;
    letter-spacing: 0.5px;
    color: var(--forest-green);
  }
</style>
</head>
<body>
<main class="brochure">
  <svg class="brochure-panels" width="1200" height="849" viewBox="0 0 1200 849" aria-hidden="true">
    <rect class="panel-forest" x="0" y="0" width="403" height="849"/>
    <polygon class="wedge-brown" points="379,0 403,0 403,849 0,849 0,785"/>
    <rect class="panel-lime" x="403" y="0" width="394" height="849"/>
    <polygon class="wedge-orange" points="403,0 429,0 771,849 403,849"/>
    <rect class="panel-paper" x="797" y="0" width="403" height="849"/>
    <polygon class="wedge-navy" points="1200,42 1200,849 825,849"/>
  </svg>

  <section class="brand-card">
    <svg class="brand-frame" width="347" height="535" viewBox="0 0 347 535" aria-hidden="true">
      <defs>
        <linearGradient id="card-fill" x1="0" y1="0" x2="0" y2="1">
          <stop offset="0" stop-color="#ffffff" stop-opacity="1"/>
          <stop offset="0.6" stop-color="#ffffff" stop-opacity="1"/>
          <stop offset="1" stop-color="#ffffff" stop-opacity="0"/>
        </linearGradient>
        <linearGradient id="card-line" x1="0" y1="0" x2="0" y2="1">
          <stop offset="0" stop-color="#33d9f2" stop-opacity="1"/>
          <stop offset="0.55" stop-color="#33d9f2" stop-opacity="0.8"/>
          <stop offset="1" stop-color="#33d9f2" stop-opacity="0"/>
        </linearGradient>
      </defs>
      <rect x="1.5" y="1.5" width="344" height="560" rx="11" fill="url(#card-fill)" stroke="url(#card-line)" stroke-width="3"/>
    </svg>
    <div class="brand-lockup">
      <span class="brand-mark"></span>
      <h1 class="brand-name">Sing Along Green Goat</h1>
    </div>
    <p class="brand-tagline">Workshops and ideas for the early years</p>
  </section>
</main>
</body>
</html>
```